Gymnastics Award Design Needed--for kids

Need a gymnastics certificate or award designed. Will be printed on a piece of 8.5x11 paper. The award will be celebrating the gymnast learning a new skill in gymnastics. So it should be fun, but still look "official". Needs to look good hanging on a gymnast's bedroom wall.

It should say "The Aerial Cartwheel Club"
I will be using this design to change it based on the skill.

My main colors are:
#34475D
#E1467A
#7555A4

So should use those, but can add others

My website is tumblenest.net so you can see the look/feel.

Target Market(s)

Main audience will be girls ages 5-12, but will also be used by slightly older girls and boys. So needs to be fun, not too gender specific.

Industry/Entity Type

Learning

Requirements
Must have
• The following will need to go on the certificate:
• * Name of Skill
• * Image of Skill
• * Gymnast's Name
• * my logo
• * Gym's Logo
• * Gym's Name
• Optional: Date

```html
<!DOCTYPE html>
<html lang="en">
<head>
<meta charset="utf-8">
<title>The Aerial Cartwheel Club – Certificate</title>
<link rel="stylesheet" href="https://fonts.googleapis.com/css2?family=Alfa+Slab+One&family=Cormorant+Garamond:ital,wght@1,500&family=Quicksand:wght@500&family=UnifrakturMaguntia&display=swap">
<style>
  :root {
    --pink: #f0607a;
    --purple: #6a46a0;
    --title-purple: #7555a4;
    --brown: #7a4a1e;
    --name-pink: #e1467a;
    --gold: #e0a94a;
    --ribbon: #6f9fbf;
    --skin-pink: #eea3a3;
    --paper: #ffffff;
  }
  * { margin: 0; padding: 0; box-sizing: border-box; }
  html, body { width: 1200px; height: 944px; overflow: hidden; background: var(--paper); }
  .certificate { position: relative; width: 1200px; height: 944px; }
  .frame { position: absolute; left: 0; top: 0; }
  .title-the, .title-club {
    position: absolute;
    font-family: "UnifrakturMaguntia", serif;
    color: var(--brown);
    font-size: 50px;
    line-height: 1;
  }
  .title-the { left: 224px; top: 108px; }
  .title-club { right: 236px; top: 246px; }
  .title-skill {
    position: absolute; left: 0; width: 1200px; top: 168px;
    text-align: center;
    font-family: "Alfa Slab One", serif;
    font-size: 62px; letter-spacing: 4px;
    color: var(--title-purple);
    line-height: 1;
  }
  .skill-art {
    position: absolute; left: 382px; top: 284px; width: 440px; height: 152px;
    background: linear-gradient(90deg, var(--skin-pink), #f4c9a8, var(--skin-pink));
    border-radius: 6px;
    opacity: .8;
  }
  .medal {
    position: absolute; top: 398px; width: 76px; height: 120px;
    background: linear-gradient(180deg, var(--ribbon) 0 55%, var(--gold) 55% 100%);
    border-radius: 8px 8px 38px 38px;
  }
  .medal--left { left: 122px; }
  .medal--right { left: 962px; }
  .presentation {
    position: absolute; left: 0; width: 1200px; top: 525px;
    text-align: center;
    font-family: "Cormorant Garamond", serif; font-style: italic; font-weight: 500;
    color: var(--brown);
  }
  .presented-line { font-size: 40px; letter-spacing: 2px; line-height: 60px; }
  .recipient {
    font-family: "UnifrakturMaguntia", serif; font-style: normal;
    color: var(--name-pink); font-size: 48px; letter-spacing: 3px;
  }
  .issuer-line { font-size: 38px; letter-spacing: 3px; line-height: 64px; }
  .award-date { font-size: 36px; letter-spacing: 3px; color: var(--name-pink); line-height: 56px; }
  .gym-mark {
    position: absolute; left: 266px; top: 748px;
    display: flex; flex-direction: column; align-items: center; gap: 14px;
    font-family: "Quicksand", sans-serif; font-weight: 500; font-size: 24px; color: #222;
  }
  .gym-mark__square { width: 52px; height: 52px; background: var(--purple); }
  .brand-mark {
    position: absolute; left: 716px; top: 808px;
    font-family: "Quicksand", sans-serif; font-weight: 500; font-size: 24px;
    color: var(--title-purple); letter-spacing: 1px;
  }
</style>
</head>
<body>
<main class="certificate">
  <svg class="frame" width="1200" height="944" viewBox="0 0 1200 944" aria-hidden="true">
    <defs>
      <clipPath id="sheet"><rect x="52" y="50" width="1093" height="843"/></clipPath>
    </defs>
    <g clip-path="url(#sheet)">
      <rect x="52" y="50" width="1093" height="420" fill="var(--pink)"/>
      <rect x="52" y="470" width="1093" height="423" fill="var(--purple)"/>
      <g fill="var(--paper)">
        <circle cx="600" cy="300" r="420"/>
        <circle cx="360" cy="480" r="310"/>
        <circle cx="840" cy="480" r="310"/>
        <circle cx="600" cy="700" r="520"/>
      </g>
    </g>
    <line x1="275" y1="440" x2="920" y2="440" stroke="var(--purple)" stroke-width="5"/>
  </svg>

  <h1>
    <span class="title-the">The</span>
    <span class="title-skill">AERIAL CARTWHEEL</span>
    <span class="title-club">Club</span>
  </h1>

  <div class="skill-art" role="img" aria-label="Illustration of a gymnast performing an aerial cartwheel in five stages"></div>
  <div class="medal medal--left" role="img" aria-label="Gold medal on a blue ribbon"></div>
  <div class="medal medal--right" role="img" aria-label="Gold medal on a blue ribbon"></div>

  <section class="presentation">
    <p class="presented-line">Presented to : <span class="recipient">Lily Carter</span></p>
    <p class="issuer-line">by Maple Street Gymnastics Gym on this day</p>
    <p class="award-date">February 17 2017</p>
  </section>

  <div class="gym-mark">
    <span class="gym-mark__square"></span>
    <span>Maple Street Gym</span>
  </div>
  <div class="brand-mark">TumbleNest</div>
</main>
</body>
</html>
```